Banner Graphics For Zelkor Storefront Page

Hello,
I am looking for a designer to help me with a banner heading that I want to place on my Zelkor storefront page. My company sells outdoor kitchen/bbq island accessories. I would like for it to have a background photo with text/logo & graphics overlaid on the image. If possible I would like it to include the 5 small "benefit boxes" that are attached on the file that features graphics for one of the products that I sell . I have also included a color photo of my products in actual use. Feel free to use it but if you have a better idea of a background image feel free to try it, maybe a lifestyle stock photo?? Or maybe something else?? I am open to all ideas and you are the creative ones:) Feel free to be creative. The pixel requirements for final image is 3,000 pixels by 600 pixels. Let me know if you have any questions. THANKS! P.s. I also included some stock photos that I like to give you some ideas.

```html
<!DOCTYPE html>
<html lang="en">
<head>
<meta charset="utf-8">
<title>Halden Outdoor Kitchens – Zelkor Storefront Banners</title>
<link rel="stylesheet" href="https://fonts.googleapis.com/css2?family=Cinzel:wght@400&family=Tinos:wght@400;700&family=Roboto:wght@700&display=swap">
<style>
  :root {
    --page-bg: #dcdcdc;
    --page-glow: #f6f6f6;
    --photo-dark: #2a2a2a;
    --photo-mid: #3c3c3c;
    --photo-warm: #4a4038;
    --orange-bright: #ff8512;
    --orange-warm: #f49d1f;
    --ink: #141414;
    --white: #ffffff;
    --badge-fill: #262a2b;
    --badge-edge: #5fc0bd;
    --badge-top: #f2f2f2;
    --badge-mark: #3a3a3a;
  }
  * { box-sizing: border-box; margin: 0; padding: 0; }
  html, body { width: 1200px; height: 1200px; overflow: hidden; }
  body {
    position: relative;
    background: radial-gradient(ellipse at 50% 50%, var(--page-glow) 0%, var(--page-bg) 75%);
    font-family: "Tinos", "Times New Roman", serif;
  }
  .banner {
    position: absolute;
    left: 31px;
    width: 1136px;
    height: 227px;
    overflow: hidden;
    box-shadow: 0 1px 3px rgba(0,0,0,0.25);
  }
  .banner--grill-1 { top: 73px; }
  .banner--grill-2 { top: 349px; }
  .banner--kitchen-1 { top: 625px; }
  .banner--kitchen-2 { top: 901px; }

  .banner__photo { position: absolute; inset: 0; }
  .photo--grill {
    background:
      radial-gradient(ellipse 60% 70% at 45% 60%, rgba(90,80,70,0.55), transparent 70%),
      linear-gradient(180deg, var(--photo-mid) 0%, var(--photo-dark) 100%);
  }
  .photo--grill-warm {
    background:
      radial-gradient(ellipse 50% 60% at 55% 65%, rgba(110,85,60,0.5), transparent 70%),
      linear-gradient(180deg, #33373c 0%, #25272a 100%);
  }
  .photo--kitchen {
    background:
      radial-gradient(ellipse 40% 50% at 80% 40%, rgba(80,80,80,0.4), transparent 70%),
      linear-gradient(180deg, #353535 0%, #2a2a2a 60%, #232323 100%);
  }

  .banner__panel {
    position: absolute; inset: 0;
    clip-path: polygon(0 0, 374px 0, 314px 100%, 0 100%);
  }
  .banner__edge {
    position: absolute; inset: 0;
    background: linear-gradient(90deg, #8a8a8a, #e6e6e6);
    clip-path: polygon(372px 0, 380px 0, 320px 100%, 312px 100%);
  }
  .banner--grill-2 .banner__panel { background: var(--orange-bright); }
  .banner--kitchen-2 .banner__panel { background: var(--orange-warm); clip-path: polygon(0 0, 374px 0, 316px 100%, 0 100%); }
  .banner--kitchen-2 .banner__edge { background: var(--white); clip-path: polygon(372px 0, 377px 0, 319px 100%, 314px 100%); }

  .brand {
    position: absolute;
    left: 40px;
    top: 70px;
    color: var(--white);
    font-family: "Cinzel", "Times New Roman", serif;
    text-align: left;
  }
  .banner--grill-2 .brand, .banner--kitchen-2 .brand { color: var(--ink); left: 46px; }
  .brand__name {
    display: block;
    font-size: 72px;
    line-height: 1;
    letter-spacing: -1px;
  }
  .brand__tagline {
    display: block;
    margin-top: 10px;
    font-family: "Tinos", "Times New Roman", serif;
    font-size: 19px;
    letter-spacing: 4.3px;
  }

  .headline {
    position: absolute;
    left: 340px;
    width: 450px;
    top: 82px;
    text-align: center;
    color: var(--white);
  }
  .headline__top, .headline__main {
    display: block;
    font-family: "Cinzel", "Times New Roman", serif;
    font-size: 33px;
    line-height: 43px;
    letter-spacing: 0.5px;
  }
  .headline__main { font-size: 34px; word-spacing: 6px; }
  .headline__sub {
    display: block;
    margin-top: 2px;
    font-family: "Tinos", "Times New Roman", serif;
    font-size: 15.5px;
    line-height: 20px;
  }
  .banner--grill-1 .headline { left: 330px; }

  .benefits {
    position: absolute;
    top: 84px;
    left: 840px;
    display: flex;
    gap: 5px;
    list-style: none;
  }
  .banner--grill-1 .benefits { left: 839px; }
  .benefit {
    width: 47px;
    height: 84px;
    border: 1.5px solid var(--badge-edge);
    border-radius: 4px;
    background: var(--badge-fill);
    overflow: hidden;
    text-align: center;
    color: var(--white);
  }
  .benefit__top {
    height: 40px;
    background: var(--badge-top);
    display: flex;
    align-items: center;
    justify-content: center;
  }
  .benefit__mark--circle { width: 30px; height: 30px; border-radius: 50%; background: var(--badge-mark); }
  .benefit__mark--square { width: 32px; height: 26px; background: var(--badge-mark); }
  .benefit__label {
    display: block;
    background: #0f0f0f;
    font-family: "Roboto", Arial, sans-serif;
    font-size: 5.5px;
    line-height: 9px;
    letter-spacing: 0.2px;
  }
  .benefit__text {
    display: block;
    padding: 3px 2px 0;
    font-family: "Roboto", Arial, sans-serif;
    font-size: 4.5px;
    line-height: 5.5px;
  }
</style>
</head>
<body>

<section class="banner banner--grill-1">
  <div class="banner__photo photo--grill" role="img" aria-label="Dark photo of sausages and meat on a barbecue grill"></div>
  <div class="brand">
    <span class="brand__name">HALDEN</span>
    <span class="brand__tagline">outdoor kitchens</span>
  </div>
  <div class="headline">
    <span class="headline__top">HAND CRAFTED</span>
    <span class="headline__main">BBQ ACCESS DOORS</span>
    <span class="headline__sub">ELEGANT DESIGN WITH DURABLE CONSTRUCTION</span>
  </div>
  <ul class="benefits">
    <li class="benefit"><div class="benefit__top"><span class="benefit__mark--circle"></span></div><span class="benefit__label">QUALITY</span><span class="benefit__text">Our team takes pride in work</span></li>
    <li class="benefit"><div class="benefit__top"><span class="benefit__mark--square"></span></div><span class="benefit__label">VALUE</span><span class="benefit__text">Heavier than the competition</span></li>
    <li class="benefit"><div class="benefit__top"><span class="benefit__mark--square"></span></div><span class="benefit__label">STRENGTH</span><span class="benefit__text">Higher corrosion resistance</span></li>
    <li class="benefit"><div class="benefit__top"><span class="benefit__mark--square"></span></div><span class="benefit__label">DURABILITY</span><span class="benefit__text">Thick stainless steel build</span></li>
    <li class="benefit"><div class="benefit__top"><span class="benefit__mark--circle"></span></div><span class="benefit__label">PEACE OF MIND</span><span class="benefit__text">Satisfaction is our priority</span></li>
  </ul>
</section>

<section class="banner banner--grill-2">
  <div class="banner__photo photo--grill-warm" role="img" aria-label="Photo of food cooking on a barbecue grill with a hand turning it"></div>
  <div class="banner__edge"></div>
  <div class="banner__panel"></div>
  <div class="brand">
    <span class="brand__name">HALDEN</span>
    <span class="brand__tagline">outdoor kitchens</span>
  </div>
  <div class="headline">
    <span class="headline__top">HAND CRAFTED</span>
    <span class="headline__main">BBQ ACCESS DOORS</span>
    <span class="headline__sub">ELEGANT DESIGN WITH DURABLE CONSTRUCTION</span>
  </div>
  <ul class="benefits">
    <li class="benefit"><div class="benefit__top"><span class="benefit__mark--circle"></span></div><span class="benefit__label">QUALITY</span><span class="benefit__text">Our team takes pride in work</span></li>
    <li class="benefit"><div class="benefit__top"><span class="benefit__mark--square"></span></div><span class="benefit__label">VALUE</span><span class="benefit__text">Heavier than the competition</span></li>
    <li class="benefit"><div class="benefit__top"><span class="benefit__mark--square"></span></div><span class="benefit__label">STRENGTH</span><span class="benefit__text">Higher corrosion resistance</span></li>
    <li class="benefit"><div class="benefit__top"><span class="benefit__mark--square"></span></div><span class="benefit__label">DURABILITY</span><span class="benefit__text">Thick stainless steel build</span></li>
    <li class="benefit"><div class="benefit__top"><span class="benefit__mark--circle"></span></div><span class="benefit__label">PEACE OF MIND</span><span class="benefit__text">Satisfaction is our priority</span></li>
  </ul>
</section>

<section class="banner banner--kitchen-1">
  <div class="banner__photo photo--kitchen" role="img" aria-label="Dark photo of an outdoor kitchen with stainless access doors and a sink"></div>
  <div class="brand">
    <span class="brand__name">HALDEN</span>
    <span class="brand__tagline">outdoor kitchens</span>
  </div>
  <div class="headline">
    <span class="headline__top">HAND CRAFTED</span>
    <span class="headline__main">BBQ ACCESS DOORS</span>
    <span class="headline__sub">ELEGANT DESIGN WITH DURABLE CONSTRUCTION</span>
  </div>
  <ul class="benefits">
    <li class="benefit"><div class="benefit__top"><span class="benefit__mark--circle"></span></div><span class="benefit__label">QUALITY</span><span class="benefit__text">Our team takes pride in work</span></li>
    <li class="benefit"><div class="benefit__top"><span class="benefit__mark--square"></span></div><span class="benefit__label">VALUE</span><span class="benefit__text">Heavier than the competition</span></li>
    <li class="benefit"><div class="benefit__top"><span class="benefit__mark--square"></span></div><span class="benefit__label">STRENGTH</span><span class="benefit__text">Higher corrosion resistance</span></li>
    <li class="benefit"><div class="benefit__top"><span class="benefit__mark--square"></span></div><span class="benefit__label">DURABILITY</span><span class="benefit__text">Thick stainless steel build</span></li>
    <li class="benefit"><div class="benefit__top"><span class="benefit__mark--circle"></span></div><span class="benefit__label">PEACE OF MIND</span><span class="benefit__text">Satisfaction is our priority</span></li>
  </ul>
</section>

<section class="banner banner--kitchen-2">
  <div class="banner__photo photo--kitchen" role="img" aria-label="Dark photo of an outdoor kitchen with stainless access doors and a sink"></div>
  <div class="banner__edge"></div>
  <div class="banner__panel"></div>
  <div class="brand">
    <span class="brand__name">HALDEN</span>
    <span class="brand__tagline">outdoor kitchens</span>
  </div>
  <div class="headline">
    <span class="headline__top">HAND CRAFTED</span>
    <span class="headline__main">BBQ ACCESS DOORS</span>
    <span class="headline__sub">ELEGANT DESIGN WITH DURABLE CONSTRUCTION</span>
  </div>
  <ul class="benefits">
    <li class="benefit"><div class="benefit__top"><span class="benefit__mark--circle"></span></div><span class="benefit__label">QUALITY</span><span class="benefit__text">Our team takes pride in work</span></li>
    <li class="benefit"><div class="benefit__top"><span class="benefit__mark--square"></span></div><span class="benefit__label">VALUE</span><span class="benefit__text">Heavier than the competition</span></li>
    <li class="benefit"><div class="benefit__top"><span class="benefit__mark--square"></span></div><span class="benefit__label">STRENGTH</span><span class="benefit__text">Higher corrosion resistance</span></li>
    <li class="benefit"><div class="benefit__top"><span class="benefit__mark--square"></span></div><span class="benefit__label">DURABILITY</span><span class="benefit__text">Thick stainless steel build</span></li>
    <li class="benefit"><div class="benefit__top"><span class="benefit__mark--circle"></span></div><span class="benefit__label">PEACE OF MIND</span><span class="benefit__text">Satisfaction is our priority</span></li>
  </ul>
</section>

</body>
</html>
```